Bluecrest Wellness Group Website

Need a informative, detailed and functional website for a medical cannabis clinic website

check out www.dumelvaclinic.com as competition - want better site than they have

Target Market(s)

Patients

Industry/Entity Type

Health Care

Number of Pages Required

1 page

Font styles to use
Sans Serif

Colors
cadf82
abd036
9bcb3b
3276b5
33a6d7
0392cd
f68d4e

Requirements
Must have
• Clean / Informative
• Will add additional educational content on opioid reduction
Nice to have
• like the white contrast with black/slate dividers. Green logo looks good on slate
• Check documents for ppt regarding website ideas
Should not have
• too many words

```html
<!DOCTYPE html>
<html lang="en">
<head>
<meta charset="utf-8">
<title>Bluecrest Wellness Group</title>
<link href="https://fonts.googleapis.com/css2?family=Lato:wght@400;700;900&family=Yellowtail&display=swap" rel="stylesheet">
<style>
:root{
  --green:#9bcb3b;
  --green-light:#cadf82;
  --green-mid:#abd036;
  --blue:#0392cd;
  --blue-sky:#33a6d7;
  --blue-deep:#3276b5;
  --orange:#f68d4e;
  --text:#444;
  --white:#fff;
}
*{margin:0;padding:0;box-sizing:border-box}
html,body{width:836px;height:1200px;overflow:hidden;background:var(--white);font-family:'Lato',sans-serif;color:var(--text)}
.page{position:relative;width:836px;height:1200px}
.header{position:absolute;top:0;left:0;width:836px;height:76px}
.brand{position:absolute;left:12px;top:14px;display:flex;align-items:center;gap:8px}
.brand-dot{width:30px;height:30px;border-radius:50%;background:var(--green)}
.brand-name{font-size:15px;font-weight:700;letter-spacing:2px;color:var(--green);line-height:1.15;text-transform:uppercase;width:150px}
.nav{position:absolute;top:33px;left:476px;display:flex;gap:16px;font-size:8.5px}
.nav a{color:#555;text-decoration:none}
.nav a.active{color:var(--blue);font-weight:700}
.phone{position:absolute;top:17px;right:17px;font-size:8.5px;font-weight:700;color:var(--blue);display:flex;align-items:center;gap:3px}
.cta-top{position:absolute;top:31px;right:0;background:var(--orange);color:#fff;font-size:7px;font-weight:700;padding:4px 7px;border-radius:8px 0 0 8px}
.search{position:absolute;top:34px;left:728px}
.hero{position:absolute;top:76px;left:0;width:836px;height:382px;background:linear-gradient(100deg,#c57a6a 0%,#d88c8a 35%,#9a8a4a 65%,#5c7a3a 100%)}
.hero-edge{position:absolute;left:0;width:836px;height:16px}
.hero-copy{position:absolute;top:148px;width:836px;text-align:center;color:#fff}
.hero-script{font-family:'Yellowtail',cursive;font-size:30px;color:var(--green-light)}
.hero-lead{font-size:20px;font-weight:700;line-height:1.4;margin-top:2px}
.arrow{position:absolute;top:180px}
.dots{position:absolute;top:338px;left:394px;display:flex;gap:6px}
.dots span{width:7px;height:7px;border-radius:50%;background:#fff}
.dots span:first-child{background:none;border:1px solid #fff}
.steps{position:absolute;top:491px;left:144px;display:flex;gap:17px}
.step{width:174px;height:152px;color:#fff;text-align:center;padding:20px 9px 0;position:relative}
.step h3{font-size:10.5px;font-weight:700;text-transform:uppercase;margin-bottom:6px}
.step p{font-size:7px;line-height:1.5}
.step .btn{position:absolute;bottom:12px;left:50%;transform:translateX(-50%);background:#fff;font-size:8.5px;font-weight:700;padding:7px 10px;border-radius:14px;white-space:nowrap}
.step-doctor{background:linear-gradient(135deg,#f6a06a,var(--orange))}
.step-doctor .btn{color:var(--orange)}
.step-card{background:linear-gradient(135deg,#4fb6e0,var(--blue-sky))}
.step-card .btn{color:var(--blue)}
.step-follow{background:linear-gradient(135deg,#b8d860,var(--green))}
.step-follow .btn{color:var(--green)}
.intro-title{position:absolute;top:672px;width:836px;text-align:center;font-size:16px;font-weight:700;color:var(--blue)}
.features{position:absolute;top:718px;left:144px;display:flex;gap:17px}
.feature{width:174px;text-align:center}
.feature svg{display:block;margin:0 auto;height:38px}
.feature h4{font-size:12px;font-weight:700;margin:10px 0 6px}
.feature p{font-size:7px;line-height:1.55;color:#555}
.f-fee h4{color:var(--orange)}
.f-doc h4{color:var(--blue)}
.f-conv h4{color:var(--green)}
.signup{position:absolute;top:866px;left:0;width:836px;height:228px;background:linear-gradient(110deg,#5a5f63,#6d7276 50%,#555b60);color:#fff;text-align:center}
.signup h2{font-size:17px;font-weight:700;color:var(--green);margin-top:32px}
.signup .note{font-size:7px;margin-top:6px}
.signup-form{display:flex;justify-content:center;gap:8px;margin-top:14px}
.signup-form .field{width:282px;height:23px;border:1px solid #ccc;border-radius:2px;background:rgba(255,255,255,.15);font-size:6px;text-align:left;padding:7px 8px}
.signup-form .submit{background:var(--green);font-size:8px;font-weight:700;padding:7px 10px}
.signup h3{font-size:16px;font-weight:700;margin-top:30px}
.signup .book{display:inline-block;background:var(--green);font-size:8px;font-weight:700;padding:7px 17px;margin-top:12px}
.footer{position:absolute;top:1106px;width:836px;text-align:center}
.footer-dot{width:30px;height:30px;border-radius:50%;background:var(--green);margin:0 auto 10px}
.copy{font-size:7.5px;color:var(--blue)}
.links{font-size:5.5px;color:var(--blue);margin-top:6px}
.social{display:flex;justify-content:center;gap:4px;margin-top:5px}
.social span{width:11px;height:11px;background:var(--orange);border-radius:2px}
</style>
</head>
<body>
<div class="page">
  <header class="header">
    <div class="brand"><div class="brand-dot"></div><div class="brand-name">Bluecrest Wellness Group</div></div>
    <nav class="nav"><a class="active">Home</a><a>About</a><a>Qualify</a><a>Appointments</a><a>FAQ</a><a>Contact</a></nav>
    <svg class="search" width="8" height="8" viewBox="0 0 10 10"><circle cx="4" cy="4" r="3" fill="none" stroke="#333" stroke-width="1.6"/><path d="M6.3 6.3 9.3 9.3" stroke="#333" stroke-width="1.6"/></svg>
    <div class="phone"><svg width="8" height="8" viewBox="0 0 10 10"><path d="M2 0.5 4 3 3 4.2C3.6 5.6 4.6 6.5 5.8 7L7 6 9.5 8 8.5 9.5C4.5 9.5 0.5 5.5 0.5 1.5Z" fill="#0392cd"/></svg>555-014-2290</div>
    <div class="cta-top">BOOK AN APPOINTMENT</div>
  </header>

  <section class="hero" role="img" aria-label="Photo of a masked researcher with a tablet inspecting cannabis plants">
    <svg class="hero-edge" style="top:-2px" viewBox="0 0 836 16" preserveAspectRatio="none"><path d="M0 0H836V10L780 4 720 12 650 5 590 11 520 4 450 12 380 6 300 12 230 5 160 11 90 4 30 12 0 6Z" fill="#fff"/></svg>
    <svg class="arrow" style="left:10px" width="12" height="20" viewBox="0 0 12 20"><path d="M10 2 2 10 10 18" fill="none" stroke="#fff" stroke-width="2"/></svg>
    <svg class="arrow" style="right:10px" width="12" height="20" viewBox="0 0 12 20"><path d="M2 2 10 10 2 18" fill="none" stroke="#fff" stroke-width="2"/></svg>
    <div class="hero-copy">
      <div class="hero-script">100% Risk Free</div>
      <div class="hero-lead">Absolutely NO fee is due if our marijuana<br>doctor does not qualify you for a medical marijuana card.</div>
    </div>
    <div class="dots"><span></span><span></span><span></span><span></span><span></span></div>
    <svg class="hero-edge" style="bottom:-2px" viewBox="0 0 836 16" preserveAspectRatio="none"><path d="M0 16H836V6L770 12 700 4 630 10 560 3 490 11 420 5 350 12 280 4 210 10 140 3 70 11 0 5Z" fill="#fff"/></svg>
  </section>

  <section class="steps">
    <div class="step step-doctor">
      <h3>Meet a Marijuana Doctor</h3>
      <p>Take our quick online medical marijuana card eligibility survey then book an appointment via phone or online to meet with one of our medical marijuana doctors.</p>
      <span class="btn">Book An Appointment</span>
    </div>
    <div class="step step-card">
      <h3>Apply for Marijuana Card</h3>
      <p>You can apply for your marijuana card at the State Health Department (SHD) website or send your completed Arkansas marijuana card application directly to the state.</p>
      <span class="btn">Apply Online at SHD</span>
    </div>
    <div class="step step-follow">
      <h3>Follow-Up Appointment</h3>
      <p>Arkansas law requires patients meet with their medical marijuana doctor within 12 months to keep their marijuana card active. Your qualified medical condition(s) must be re-certified by a marijuana doctor or your marijuana card will expire.</p>
      <span class="btn">Book Follow Up</span>
    </div>
  </section>

  <h2 class="intro-title">The One &amp; Only Specialized Marijuana Doctor Clinic</h2>

  <section class="features">
    <div class="feature f-fee">
      <svg viewBox="0 0 50 34" width="50"><rect x="1" y="3" width="48" height="28" rx="3" fill="#f68d4e"/><ellipse cx="25" cy="17" rx="8" ry="7" fill="#fff"/></svg>
      <h4>No Qualification? No Fee</h4>
      <p>We offer 100% risk free in-office consultations with one of our marijuana doctors. If you do not qualify for a marijuana card, you do not pay. It's that simple. Some of our competitors still charge a fee if you do not qualify for a marijuana card.</p>
    </div>
    <div class="feature f-doc">
      <svg viewBox="0 0 34 38" width="34"><circle cx="17" cy="9" r="8" fill="#0392cd"/><path d="M2 37V30C2 23 8 20 17 20S32 23 32 30V37Z" fill="#0392cd"/><circle cx="12" cy="30" r="3" fill="none" stroke="#fff" stroke-width="1.5"/><circle cx="22" cy="30" r="3" fill="none" stroke="#fff" stroke-width="1.5"/></svg>
      <h4>Qualified Physicians</h4>
      <p>We partner with only the best marijuana doctors in Arkansas. Our marijuana doctors are not only highly qualified but they understand that medical marijuana is a revolutionary new medicine that can improve quality of life for patients in the 21st century.</p>
    </div>
    <div class="feature f-conv">
      <svg viewBox="0 0 40 34" width="40"><path d="M2 22 14 8 24 10 38 4 36 16 24 26 12 30Z" fill="#9bcb3b"/><path d="M16 14 26 14 24 20 18 20" fill="none" stroke="#fff" stroke-width="1.8"/></svg>
      <h4>Convenience</h4>
      <p>We are conveniently located in the heart of the Westbrook retail district at the corner of Elm and Carver Road. We are directly across the street from the Harlow's. With our three-click online appointments, meeting face to face with one of our marijuana doctors is as easy as 1-2-3.</p>
    </div>
  </section>

  <section class="signup" role="img" aria-label="Photo of a doctor in a white coat reviewing a document, darkened behind the text">
    <h2>Sign up for our Newsletter</h2>
    <p class="note">Please subscribe and receive our latest news, promotions, events, and clinic updates you can't get anywhere else.</p>
    <div class="signup-form"><div class="field">Enter your Email here*</div><div class="submit">Subscribe Now</div></div>
    <h3>Meet with one of our Marijuana Doctors</h3>
    <span class="book">Book Now</span>
  </section>

  <footer class="footer">
    <div class="footer-dot"></div>
    <p class="copy">© 2019 by Bluecrest Wellness Group. All Rights Reserved.</p>
    <p class="links">Privacy | Terms of Use | Join Our Team</p>
    <div class="social"><span></span><span></span><span></span><span></span><span></span></div>
  </footer>
</div>
</body>
</html>
```